Attorney Business Card

I need a business card that looks professional yet modern. I am an Attorney. , I need a professional yet modern business card for my law practice. My logo and information have been uploaded. , I need a business card that looks professional yet modern. I am an Attorney. , I need a professional yet modern business card for my law practice. My logo and information have been uploaded.

Industry/Entity Type

Business

Requirements
Must have
• My logo which has been uploaded , my logo , My logo which has been uploaded , my logo

```html
<!DOCTYPE html>
<html lang="en">
<head>
<meta charset="utf-8">
<title>Marrow Law Firm — Business Card</title>
<link rel="stylesheet" href="https://fonts.googleapis.com/css2?family=Oswald:wght@400;500;700&family=Roboto+Condensed:wght@400;700&display=swap">
<style>
  :root {
    --page-bg: #e6e7e9;
    --card-bg: #2a2b2e;
    --card-bg-deep: #1f2023;
    --accent: #3fb4e0;
    --accent-soft: #8fd5f0;
    --text-main: #f4f5f7;
    --text-muted: #9a9ca1;
  }
  * { margin: 0; padding: 0; box-sizing: border-box; }
  html, body { width: 1200px; height: 1000px; overflow: hidden; }
  body {
    background: var(--page-bg);
    font-family: "Oswald", "Arial Narrow", sans-serif;
    display: flex;
    flex-direction: column;
    align-items: center;
    justify-content: center;
    gap: 56px;
  }
  .card {
    position: relative;
    width: 700px;
    height: 400px;
    background: radial-gradient(ellipse at 40% 30%, var(--card-bg) 0%, var(--card-bg-deep) 100%);
    border-radius: 6px;
    box-shadow: 0 12px 30px rgba(0,0,0,.28);
    overflow: hidden;
    color: var(--text-main);
  }

  /* brand lockup (stand-in for the firm mark) */
  .brand {
    position: absolute;
    display: flex;
    align-items: center;
    gap: 10px;
  }
  .brand-dot {
    width: 16px; height: 16px;
    border-radius: 50%;
    background: var(--accent);
  }
  .brand-name {
    font-family: "Oswald", sans-serif;
    font-weight: 500;
    color: var(--accent-soft);
    font-size: 20px;
    letter-spacing: 2px;
    text-transform: uppercase;
  }

  /* ---------- contact side ---------- */
  .card--contact .brand { top: 40px; right: 44px; }
  .card--contact .corner-lines {
    position: absolute; top: 92px; right: 0;
    width: 36px; height: 10px;
    border-top: 3px solid var(--accent);
    border-bottom: 3px solid var(--accent);
  }
  .side-rule {
    position: absolute; left: 34px; top: 118px;
    width: 12px; height: 120px;
    border-left: 4px solid var(--accent);
    border-right: 4px solid var(--accent);
  }
  .identity { position: absolute; left: 74px; top: 110px; }
  .identity-name {
    font-weight: 700;
    font-size: 40px;
    letter-spacing: .5px;
    line-height: 1.1;
  }
  .identity-title {
    font-family: "Roboto Condensed", sans-serif;
    font-size: 13px;
    letter-spacing: 6px;
    color: var(--text-muted);
    margin-top: 4px;
  }
  .contact-list {
    position: absolute; left: 36px; top: 232px;
    list-style: none;
    display: flex; flex-direction: column; gap: 10px;
  }
  .contact-item { display: flex; align-items: center; gap: 16px; }
  .contact-icon {
    width: 24px; height: 24px; border-radius: 50%;
    background: var(--accent);
    display: flex; align-items: center; justify-content: center;
    flex: none;
  }
  .contact-icon svg { width: 13px; height: 13px; }
  .contact-text {
    font-family: "Roboto Condensed", sans-serif;
    font-size: 17px;
    letter-spacing: .5px;
  }
  .contact-text--bold { font-family: "Oswald", sans-serif; font-weight: 700; font-size: 24px; }
  .contact-text--small { font-size: 15px; text-transform: uppercase; }

  /* ---------- name side ---------- */
  .card--name .brand { top: 120px; left: 300px; }
  .card--name .edge-lines {
    position: absolute; top: 0; right: 30px;
    width: 14px; height: 100%;
    border-left: 4px solid var(--accent);
    border-right: 4px solid var(--accent);
  }
  .front-name {
    position: absolute; left: 300px; top: 170px;
    font-weight: 700; font-size: 50px; letter-spacing: .5px;
  }
  .front-rule {
    position: absolute; height: 5px; background: var(--accent);
  }
  .front-rule--upper { left: 430px; top: 250px; width: 200px; }
  .front-rule--lower { left: 300px; top: 268px; width: 330px; }
</style>
</head>
<body>

  <section class="card card--contact" aria-label="Business card, contact side">
    <div class="brand">
      <span class="brand-dot"></span>
      <span class="brand-name">Marrow Law Firm</span>
    </div>
    <div class="corner-lines"></div>

    <div class="side-rule"></div>
    <div class="identity">
      <h1 class="identity-name">Daniel Marrow, ESQ</h1>
      <p class="identity-title">ATTORNEY AT LAW</p>
    </div>

    <ul class="contact-list">
      <li class="contact-item">
        <span class="contact-icon">
          <svg viewBox="0 0 16 16"><path d="M8 1 1 7h2v7h4v-4h2v4h4V7h2z" fill="#fff"/></svg>
        </span>
        <span class="contact-text">1820 Harbor Ave, Suite 400, Lakeside, CA 90417</span>
      </li>
      <li class="contact-item">
        <span class="contact-icon">
          <svg viewBox="0 0 16 16"><path d="M4 1 1.5 3.5c0 6 5 11 11 11L15 12l-3-2.5-2 1.5C8 10 6 8 5 6l1.5-2z" fill="#fff"/></svg>
        </span>
        <span class="contact-text contact-text--bold">555.204.1187</span>
      </li>
      <li class="contact-item">
        <span class="contact-icon">
          <svg viewBox="0 0 16 16"><rect x="1" y="3" width="14" height="10" rx="1" fill="#fff"/><path d="M1.5 3.5 8 9l6.5-5.5" stroke="#3fb4e0" stroke-width="1.4" fill="none"/></svg>
        </span>
        <span class="contact-text contact-text--small">daniel@marrowlaw.com</span>
      </li>
      <li class="contact-item">
        <span class="contact-icon">
          <svg viewBox="0 0 16 16"><rect x="4" y="1" width="8" height="14" rx="1.5" fill="#fff"/><rect x="5.5" y="3" width="5" height="8" fill="#3fb4e0"/></svg>
        </span>
        <span class="contact-text contact-text--bold">555.318.6420</span>
      </li>
    </ul>
  </section>

  <section class="card card--name" aria-label="Business card, name side">
    <div class="edge-lines"></div>
    <div class="brand">
      <span class="brand-dot"></span>
      <span class="brand-name">Marrow Law Firm</span>
    </div>
    <h2 class="front-name">Daniel Marrow</h2>
    <div class="front-rule front-rule--upper"></div>
    <div class="front-rule front-rule--lower"></div>
  </section>

</body>
</html>
```